LOS PINARES DE ORO - EXCLUSIVE AND LUXURY REAL ESTATE PROJECT

Se trata del diseño de un mono poste grande (4 m x 2 m) o (8m x 3m) anunciando la construcción de 30 villas de lujo en un terreno en primera línea de playa en el sur de España (Cádiz).

La idea es crear expectación y transmitir lujo y exclusividad.

Target Market(s)

Clientes de alto poder adquisitivo que quieran adquirir su segunda vivienda en un entorno privilegiado a escasos pasos de una de las playas más bonitas de Cádiz.

Industry/Entity Type

REAL ESTATE

Colors

Designer to choose colors to be used in the design.

Requirements
Must have
• LOS PINARES DE ORO as the name of the development
Nice to have
• Crear expectación con ideas del tipo: “Coming soon” o “No te lo puedes perder”

```html
<!DOCTYPE html>
<html lang="es">
<head>
<meta charset="utf-8">
<title>Los Pinares de Oro – Coming Soon</title>
<link rel="stylesheet" href="https://fonts.googleapis.com/css2?family=Playfair+Display:wght@700;900&family=Crimson+Text:wght@400&family=Sacramento&display=swap">
<style>
  :root {
    --navy-deep: #08203f;
    --navy: #0c2f5c;
    --sky: #5d8fc4;
    --sky-light: #9fc2e4;
    --wall-warm: #d9b56a;
    --wall-glow: #f1c65a;
    --stone: #e8e2d6;
    --lawn: #3d6a2c;
    --lawn-dark: #274a1d;
    --gold-light: #ffe27a;
    --gold: #f0b52a;
    --gold-deep: #c98a10;
    --white: #ffffff;
  }
  * { margin: 0; padding: 0; box-sizing: border-box; }
  html, body {
    width: 1200px; height: 600px; overflow: hidden;
    background: var(--navy-deep);
  }
  .billboard {
    position: relative;
    width: 1200px; height: 600px;
    overflow: hidden;
    background: linear-gradient(90deg, var(--navy-deep) 0%, var(--navy) 40%, var(--navy) 100%);
  }
  .villa-photo {
    position: absolute;
    left: 380px; top: 0;
    width: 820px; height: 600px;
    background:
      linear-gradient(180deg, transparent 0%, transparent 78%, var(--lawn) 88%, var(--lawn-dark) 100%),
      radial-gradient(ellipse 40% 30% at 58% 55%, var(--wall-glow) 0%, rgba(241,198,90,0) 100%),
      linear-gradient(180deg, var(--sky) 0%, var(--sky-light) 22%, var(--stone) 40%, var(--wall-warm) 62%, var(--stone) 80%);
    -webkit-mask-image: linear-gradient(90deg, transparent 0%, #000 30%);
            mask-image: linear-gradient(90deg, transparent 0%, #000 30%);
  }
  .title {
    position: absolute;
    left: 44px; top: 36px;
    font-family: "Playfair Display", serif;
    font-weight: 900;
    font-size: 84px;
    line-height: 106px;
    letter-spacing: -1px;
    background: linear-gradient(180deg, var(--gold-light) 0%, var(--gold) 55%, var(--gold-deep) 100%);
    -webkit-background-clip: text;
            background-clip: text;
    color: transparent;
    filter: drop-shadow(0 3px 6px rgba(0,0,0,0.35));
  }
  .title span { display: block; }
  .intro {
    position: absolute;
    left: 46px; top: 258px;
    width: 400px;
    font-family: "Crimson Text", serif;
    font-size: 21px;
    line-height: 28px;
    color: var(--white);
  }
  .teaser {
    position: absolute;
    left: 36px; top: 372px;
    font-family: "Sacramento", cursive;
    color: var(--white);
    font-size: 150px;
    line-height: 110px;
  }
  .teaser span { display: block; }
  .teaser .teaser-second { padding-left: 96px; }
</style>
</head>
<body>
  <main class="billboard">
    <div class="villa-photo" role="img" aria-label="Villa moderna de lujo de dos plantas al atardecer, con pérgola de madera, balcón de cristal, piscina, tumbona y jardín de césped"></div>

    <h1 class="title">
      <span>LOS PINARES</span>
      <span>DE ORO</span>
    </h1>

    <p class="intro">anunciando la construcción de 30 villas de lujo en un terreno en primera línea de playa en el sur de España</p>

    <p class="teaser">
      <span>Coming</span>
      <span class="teaser-second">Soon</span>
    </p>
  </main>
</body>
</html>
```